Business Card Design Project

Our slogan is "dare to be different" and we are after something creative and different to go with our company image.

Criteria:
The business card will not be a standard size but it must be small or big enough to fit in a wallet.
It will be double sided
It will have our colours and the design will be based around our logo (attached)
No fancy text just clean sharp easy to read. we have been using the stag sans book font type so this or similar type is preferable (we are not locked in a font type.

For more information about us, please visit out website at www.glimtrovale.com.au

Target Market(s)

outdoor and recreational industry/market

Industry/Entity Type

Business

Requirements
Must have
• Logo
Slogan
website
contact details (phone and email)
Name and Position
social media facebook and youtube

```html
<!DOCTYPE html>
<html lang="en">
<head>
<meta charset="utf-8">
<title>Glimtrovale – Business Card</title>
<link rel="stylesheet" href="https://fonts.googleapis.com/css2?family=Archivo:wght@400;500;700&display=swap">
<style>
  :root {
    --page: #ffffff;
    --card: #0b0c0d;
    --accent: #f0341c;
    --ink: #ffffff;
    --ghost: #3b3b3b;
    --badge: #1e1e1e;
    --rule: #000000;
  }
  html, body {
    margin: 0;
    width: 1200px;
    height: 846px;
    overflow: hidden;
    background: var(--page);
  }
  .sheet { display: block; width: 1200px; height: 846px; }
  .sheet text { font-family: "Archivo", Arial, sans-serif; }
  .card-shape { fill: var(--card); }
  .ring-accent { fill: none; stroke: var(--accent); stroke-width: 6; }
  .ring-ghost { fill: none; stroke: var(--ghost); stroke-width: 6; }
  .measure-line { stroke: var(--rule); stroke-width: 2; }
  .measure-label { font-size: 20px; font-weight: 700; fill: var(--rule); }
  .side-label { font-size: 13px; font-weight: 700; letter-spacing: 4px; fill: var(--rule); }
  .caption { font-size: 19px; font-weight: 700; fill: var(--rule); text-anchor: middle; }
  .brand-center { font-size: 21px; font-weight: 500; letter-spacing: 1px; text-anchor: middle; }
  .brand-center--accent { fill: var(--accent); }
  .brand-center--ghost { fill: var(--ghost); }
  .wordmark { font-size: 15px; font-weight: 400; letter-spacing: 1px; fill: var(--ink); }
  .slogan { font-size: 6.5px; font-weight: 500; letter-spacing: 0.8px; fill: var(--ink); }
  .contact-name { font-size: 13px; font-weight: 700; letter-spacing: 4px; fill: var(--accent); }
  .contact-line { font-size: 8.5px; font-weight: 700; letter-spacing: 2.5px; fill: var(--ink); }
  .web-line { font-size: 5.6px; font-weight: 500; letter-spacing: 0.9px; fill: var(--ink); text-anchor: end; }
  .badge { fill: var(--badge); stroke: var(--accent); stroke-width: 3; }
</style>
</head>
<body>
<svg class="sheet" viewBox="0 0 1200 846" xmlns="http://www.w3.org/2000/svg">
  <defs>
    <clipPath id="back-clip">
      <polygon points="116,234 372,300 626,234 626,526 372,460 116,526"/>
    </clipPath>
    <clipPath id="front-clip">
      <polygon points="653,234 910,300 1165,234 1165,526 910,460 653,526"/>
    </clipPath>
  </defs>

  <!-- dimensions -->
  <line class="measure-line" x1="113" y1="196" x2="627" y2="196"/>
  <text class="measure-label" x="355" y="182" text-anchor="middle">9cm</text>
  <line class="measure-line" x1="72" y1="238" x2="72" y2="524"/>
  <text class="measure-label" x="12" y="396">5cm</text>

  <!-- back side -->
  <g class="card card--back">
    <polygon class="card-shape" points="116,234 372,300 626,234 626,526 372,460 116,526"/>
    <g clip-path="url(#back-clip)">
      <circle class="ring-accent" cx="372" cy="380" r="107"/>
    </g>
    <text class="brand-center brand-center--accent" x="372" y="388">GLIMTROVALE</text>
    <text class="wordmark" x="505" y="388">GLIMTROVALE</text>
    <text class="slogan" x="505" y="398">DARE TO BE DIFFERENT</text>
  </g>

  <!-- front side -->
  <g class="card card--front">
    <polygon class="card-shape" points="653,234 910,300 1165,234 1165,526 910,460 653,526"/>
    <g clip-path="url(#front-clip)">
      <circle class="ring-ghost" cx="910" cy="380" r="107"/>
    </g>
    <text class="brand-center brand-center--ghost" x="910" y="388">GLIMTROVALE</text>

    <text class="contact-name" x="672" y="311">NAME</text>
    <text class="contact-line" x="672" y="323">POSITION</text>
    <text class="contact-line" x="672" y="347">PHONE NUMBER</text>
    <text class="contact-line" x="672" y="359">EMAIL</text>

    <circle class="badge" cx="1100" cy="346" r="44"/>
    <text class="wordmark" x="1148" y="419" text-anchor="end">GLIMTROVALE</text>
    <text class="slogan" x="1148" y="430" text-anchor="end">DARE TO BE DIFFERENT</text>
    <text class="web-line" x="1148" y="445">http://www.glimtrovale.com.au/</text>
    <text class="web-line" x="1148" y="453">www.friendbook.net/Glimtrovale</text>
    <text class="web-line" x="1148" y="461">www.vidstream.net/TheGlimtrovale</text>
  </g>

  <text class="side-label" x="116" y="586">BACK</text>
  <text class="side-label" x="654" y="586">fRONT</text>

  <text class="caption" x="607" y="755">Business card</text>
  <text class="caption" x="607" y="796">Actual size</text>
</svg>
</body>
</html>
```